Compass & Canvas needs new business card design

I need a new business card design. I'm looking for out-of-the-box design which represents the freedom of being a location independent entrepreneur.
I offer coaching, retreats and trips.
I would like to see designs with and without the photo.
Colors I use are black (#000000), green (#25A796) and brown (#D7C38C)
Website compassandcanvas.net

Target Market(s)

location independent entrepreneurs, digital nomads, people looking to swap the 9 to 5 for a lifestyle business

Industry/Entity Type

Business

Contact Information for Business Card

Daria Tolsen
Your Lifestyle Business Coach, Retreat & Trip Leader
http://compassandcanvas.net
hello@compassandcanvas.net
Live a life you don't need a holiday from

Font styles to use
Serif
Sans Serif

Requirements
Must have
• One side should contain only the logo. I would also consider having the "Live a life you don't need a holiday from" on that side too (depending on how it looks)
• Please show both sides on the designs.

```html
<!DOCTYPE html>
<html lang="en">
<head>
<meta charset="utf-8">
<title>Compass &amp; Canvas – Business Card</title>
<link href="https://fonts.googleapis.com/css2?family=Arimo:wght@400;700&display=swap" rel="stylesheet">
<style>
  :root {
    --backdrop: #e9e6e1;
    --card: #ffffff;
    --ink: #3a3a3a;
    --ink-soft: #222222;
    --teal: #25a796;
    --teal-bright: #2fbfae;
    --shadow: rgba(0, 0, 0, 0.18);
  }
  * { margin: 0; padding: 0; box-sizing: border-box; }
  html, body {
    width: 1200px; height: 902px; overflow: hidden;
    background: var(--backdrop);
    font-family: "Arimo", Arial, sans-serif;
  }
  .canvas { position: relative; width: 1200px; height: 902px; }
  .card {
    position: absolute; width: 700px; height: 400px;
    background: var(--card);
    box-shadow: 0 6px 18px var(--shadow);
    overflow: hidden;
  }
  .card--front { left: 110px; top: 40px; }
  .card--back { left: 390px; top: 470px; }

  .wordmark {
    font-weight: 700; color: var(--ink);
    letter-spacing: 1px; text-transform: uppercase; white-space: nowrap;
  }
  .card--front .wordmark {
    position: absolute; top: 110px; left: 0; width: 100%;
    text-align: center; font-size: 48px;
  }
  .tagline {
    position: absolute; top: 300px; left: 0; width: 100%;
    text-align: center; font-size: 19px; color: var(--ink-soft);
  }

  .card--back .wordmark {
    position: absolute; top: 66px; left: 48px; font-size: 28px;
    z-index: 1;
  }
  .person { position: absolute; top: 150px; left: 48px; z-index: 1; }
  .person__name { font-size: 28px; font-weight: 700; color: var(--ink); }
  .person__role {
    margin-top: 6px; font-size: 17px; line-height: 1.25; color: var(--teal-bright);
  }
  .contacts {
    position: absolute; left: 48px; bottom: 40px; list-style: none;
    font-size: 16px; color: var(--ink-soft); z-index: 1;
  }
  .contacts li { display: flex; align-items: center; gap: 10px; margin-top: 10px; }
  .contacts svg { width: 20px; height: 20px; flex: none; }
  .photo-panel { position: absolute; top: 0; right: 0; width: 300px; height: 400px; }
</style>
</head>
<body>
<main class="canvas">
  <section class="card card--front" aria-label="Card front">
    <div class="wordmark">Compass &amp; Canvas</div>
    <p class="tagline">Live a life you don't need a holiday from</p>
  </section>

  <section class="card card--back" aria-label="Card back">
    <svg class="photo-panel" viewBox="0 0 300 400" preserveAspectRatio="none">
      <defs>
        <linearGradient id="foliage" x1="0" y1="0" x2="0" y2="1">
          <stop offset="0" stop-color="#6f9a5e"/>
          <stop offset="0.55" stop-color="#9aa58a"/>
          <stop offset="1" stop-color="#8d8a78"/>
        </linearGradient>
      </defs>
      <path d="M10 0 C60 120 75 280 50 400 L300 400 L300 0 Z" fill="var(--teal-bright)"/>
      <path d="M26 0 C76 120 91 280 66 400 L300 400 L300 0 Z" fill="url(#foliage)" role="img" aria-label="Photo of the coach sitting on a wooden rail beneath leafy trees, holding a small sign"/>
    </svg>
    <div class="wordmark">Compass &amp; Canvas</div>
    <div class="person">
      <h1 class="person__name">Daria Tolsen</h1>
      <p class="person__role">Your Lifestyle Business Coach,<br>Retreat &amp; Trip Leader</p>
    </div>
    <ul class="contacts">
      <li>
        <svg viewBox="0 0 20 20" aria-hidden="true"><rect x="1" y="1" width="18" height="18" fill="#222"/><path d="M4 6h12v8H4z" fill="#fff"/><path d="M4 6l6 5 6-5" fill="none" stroke="#222" stroke-width="1.4"/></svg>
        hello@compassandcanvas.net
      </li>
      <li>
        <svg viewBox="0 0 20 20" aria-hidden="true"><rect x="1" y="1" width="18" height="18" fill="#222"/><circle cx="10" cy="10" r="5.5" fill="none" stroke="#fff" stroke-width="1.4"/><path d="M4.5 10h11M10 4.5c-2.5 3-2.5 8 0 11M10 4.5c2.5 3 2.5 8 0 11" fill="none" stroke="#fff" stroke-width="1"/></svg>
        http://compassandcanvas.net
      </li>
    </ul>
  </section>
</main>
</body>
</html>
```